silverbrook gymnastics academy

need a website for above to contain information about the academy, enrollment form etc..

Need a web design for new business Silverbrook Gymnastics Academy offering classes in gymnastics. Info on the business is in the doc called "Web design" which details the tabs I will need on my page. Please see our Facebook page to get an idea of the style Silverbrookgymnasticsacademy.

Thank you for your help. I do not require hosting of a domain name just need it all ready to be hosted. Thanks

Budget now increased to include the coding of the website as well.

```html
<!DOCTYPE html>
<html lang="en">
<head>
<meta charset="utf-8">
<title>Silverbrook Gymnastics Academy</title>
<link rel="stylesheet" href="https://fonts.googleapis.com/css2?family=Open+Sans:wght@400;600;700;800&display=swap">
<style>
:root{
  --ink:#2b2b2b;
  --muted:#666;
  --dark:#262626;
  --darker:#1a1a1a;
  --nav:#2c2c2c;
  --yellow:#f3d43c;
  --soft-yellow:#f2dc8a;
  --light:#efefef;
  --white:#fff;
}
*{box-sizing:border-box;margin:0;padding:0}
html,body{width:1200px;height:2216px;overflow:hidden}
body{font-family:"Open Sans",Arial,sans-serif;color:var(--ink);background:var(--white)}
.hero{position:relative;height:728px;background:radial-gradient(ellipse at 45% 55%,#f4e9b8 0%,#e7d58a 35%,#c9b35a 75%,#a58f3f 100%)}
.hero-art{position:absolute;inset:0}
.brand{position:absolute;top:22px;left:50%;transform:translateX(-50%);display:flex;flex-direction:column;align-items:center;gap:8px}
.brand-dot{width:110px;height:110px;border-radius:50%;background:var(--darker);display:flex;align-items:center;justify-content:center;color:var(--white);font-weight:700;font-size:34px}
.brand-name{font-weight:700;font-size:15px;color:var(--darker);letter-spacing:1px;text-transform:uppercase}
.slide-arrow{position:absolute;top:350px;width:26px;height:44px;background:rgba(0,0,0,.35);display:flex;align-items:center;justify-content:center}
.slide-arrow.left{left:0}.slide-arrow.right{right:0}
.main-nav{height:72px;background:var(--nav);display:flex;padding-left:110px}
.main-nav a{display:flex;align-items:center;justify-content:center;width:200px;color:#ddd;text-decoration:none;font-size:17px;font-weight:600;text-transform:uppercase}
.main-nav a.active{color:var(--yellow);background:var(--darker)}
.welcome{height:224px;background:var(--light);text-align:center;padding-top:40px}
h1{font-size:32px;font-weight:800;margin-bottom:14px;color:var(--ink)}
.lead{width:860px;margin:0 auto;font-size:16px;line-height:26px;color:var(--muted)}
.about{text-align:center;padding-top:52px;height:584px}
h2{font-size:28px;font-weight:700;margin-bottom:10px}
.about .lead{width:780px}
.cards{display:flex;justify-content:center;gap:46px;margin-top:48px}
.card{width:304px}
.card-photo{height:200px}
.card-photo.one{background:linear-gradient(135deg,#2d1020,#b2346a 60%,#e9a2c1)}
.card-photo.two{background:linear-gradient(135deg,#0d0d0d,#555 60%,#aaa)}
.card-photo.three{background:linear-gradient(135deg,#3a2416,#a86a3a 60%,#e3b887)}
.card-caption{height:100px;background:var(--soft-yellow);display:flex;align-items:center;justify-content:center;padding:0 22px;font-size:15px;font-weight:600;line-height:22px;color:var(--ink)}
.promo{height:328px;background:var(--dark);text-align:center;padding-top:60px}
.promo h3{color:var(--yellow);font-size:34px;font-weight:800;line-height:44px;text-transform:uppercase}
.promo p{width:780px;margin:18px auto 0;color:#cfcfcf;font-size:15px;line-height:24px}
.btn{display:inline-block;margin-top:24px;background:var(--yellow);color:var(--darker);font-weight:800;font-size:15px;padding:10px 24px;text-transform:uppercase}
.contact{height:136px;background:var(--light);padding:24px 100px 0;display:flex;justify-content:space-between}
.contact h4{font-size:18px;font-weight:600;margin-bottom:12px}
.contact-items{display:flex;gap:50px}
.contact-item{display:flex;align-items:center;gap:12px;font-size:13px;line-height:18px;color:var(--muted)}
.icon{width:34px;height:34px;border-radius:50%;background:#555;display:flex;align-items:center;justify-content:center;flex:none}
.follow{text-align:left}
.social{display:flex;gap:10px}
.social span{width:34px;height:34px;border-radius:4px}
.social .s1{background:#3b5998}.social .s2{background:#1f7bc1}.social .s3{background:#d8352a}
.footer{height:144px;background:var(--darker);text-align:center;padding-top:30px;color:#bbb;font-size:14px}
.footer-links{display:flex;justify-content:center;gap:60px;margin-bottom:40px}
.footer-links a{color:#bbb;text-decoration:none}
</style>
</head>
<body>
<header class="hero">
  <div class="hero-art" role="img" aria-label="Photo of a young gymnast leaping in a split on the balance beam"></div>
  <div class="brand"><div class="brand-dot">SGA</div><div class="brand-name">Silverbrook Gymnastics Academy</div></div>
  <div class="slide-arrow left"><svg width="12" height="20"><path d="M10 2 2 10l8 8" stroke="#fff" stroke-width="3" fill="none"/></svg></div>
  <div class="slide-arrow right"><svg width="12" height="20"><path d="M2 2l8 8-8 8" stroke="#fff" stroke-width="3" fill="none"/></svg></div>
</header>
<nav class="main-nav">
  <a class="active" href="#">Home</a><a href="#">Forms</a><a href="#">More Info</a><a href="#">Policies</a><a href="#">Contact Us</a>
</nav>
<section class="welcome">
  <h1>WELCOME TO SILVERBROOK GYMNASTICS ACADEMY (SGA)</h1>
  <p class="lead">Gymnastics is for everyone, people of all ages, shapes, sizes and capabilities can participate in and enjoy gymnastics. We offer classes from Kindergym to Adult classes. SGA is a fully affiliated club and our coaches are accredited and qualified with National Gymnastics Council.</p>
</section>
<section class="about">
  <h2>About us</h2>
  <p class="lead">SGA is newly established family business whose mission is to provide high quality gymnastics programs in a wide variety of activities to suit all ages, levels and ability. Our vision is to become one of the most successful and holistic gymnastics clubs in Sydney.</p>
  <div class="cards">
    <div class="card"><div class="card-photo one" role="img" aria-label="Photo of a gymnast posing in a pink leotard"></div><div class="card-caption">A family friendly and supportive environment for all gymnasts to enjoy</div></div>
    <div class="card"><div class="card-photo two" role="img" aria-label="Photo of a gymnast performing on the bars"></div><div class="card-caption">High quality, dedicated and motivated coaches</div></div>
    <div class="card"><div class="card-photo three" role="img" aria-label="Photo of a gymnast balancing on the beam"></div><div class="card-caption">Progressive and enjoyable recreation, development and competitive gymnastics programs</div></div>
  </div>
</section>
<section class="promo">
  <h3>Donec a erat at orci fermentum laoreet<br>November 26, 2014</h3>
  <p>Pellentesque vel libero lacinia, commodo libero sit, placerat mauris. Nullam aliquet congue arcu, et euismod nunc pellentesque id. In vehicula pharetra leo et vulputate. In eleifend quis elit non dapibus. Integer nec enim tempor, fringilla leo vel, ultrices mi.</p>
  <span class="btn">Know more</span>
</section>
<section class="contact">
  <div>
    <h4>Contact us</h4>
    <div class="contact-items">
      <div class="contact-item"><span class="icon"><svg width="14" height="18"><path d="M7 1a6 6 0 0 1 6 6c0 4-6 10-6 10S1 11 1 7a6 6 0 0 1 6-6z" fill="#fff"/><circle cx="7" cy="7" r="2" fill="#555"/></svg></span><span>55 Building name<br>Street name, City<br>Zip code</span></div>
      <div class="contact-item"><span class="icon"><svg width="16" height="16"><path d="M3 1l3 3-2 2c1 2 3 4 5 5l2-2 3 3-2 3C7 15 1 9 1 3z" fill="#fff"/></svg></span><span>555 213 0148</span></div>
      <div class="contact-item"><span class="icon"><svg width="16" height="16"><path d="M3 1l3 3-2 2c1 2 3 4 5 5l2-2 3 3-2 3C7 15 1 9 1 3z" fill="#fff"/></svg></span><span>555 231 0648</span></div>
      <div class="contact-item"><span class="icon"><svg width="18" height="14"><rect x="1" y="1" width="16" height="12" fill="none" stroke="#fff" stroke-width="2"/><path d="M1 1l8 7 8-7" stroke="#fff" stroke-width="2" fill="none"/></svg></span><span>info@silverbrookga.com</span></div>
    </div>
  </div>
  <div class="follow">
    <h4>Follow us on</h4>
    <div class="social"><span class="s1"></span><span class="s2"></span><span class="s3"></span></div>
  </div>
</section>
<footer class="footer">
  <div class="footer-links"><a href="#">• Home</a><a href="#">• Forms</a><a href="#">• More Info</a><a href="#">• Policies</a><a href="#">• Contact us</a></div>
  <p>Copyright © 2014 Silverbrook Gymnastics Academy. All rights reserved.</p>
</footer>
</body>
</html>
```